Halden Pelvic Care Clinics needs promo/informational brochure for marketing

Our practice has added a new practitioner and our goal is to highlight her (Nell Brisco, PA-C) in this marketing campaign while providing useful information about the practice and conditions we treat. We have also closed our Maryland Office and moved to a new NY office (7 E. 81st St. Suite 512 NY, NY 10028). I have included a copy of what our last brochure looked like as an example of what I absolutely despise:) We are removing Loretta Quince from the brochure and adding a book (also attached). We want something modern, concise, streamlined, and professional. We would love to see what you all can come up with! The sooner we get responses, the better!

Target Market(s)

physicians and patients

Industry/Entity Type

Medical

Font styles to use
Other font styles liked:
• avenir book? i'll leave it to the designer!

Colors
ffffff
cee9f5
e4daeb
000000
9d9d9d
cbcbcb

Requirements
Must have
• some sort of lotus image....or some type of background from stock images
• This is the bio of Nell Brisco to be included:
• Nell Brisco, PA
• Nell Brisco is a Nationally Certified Physician Assistant licensed in New York and Washington, DC. She graduated with honors from Wexley College of Health Sciences where she was awarded the prestigious Pemberton Award.
• Nell has been treating women with sexual dysfunction since 2010. She has extensive experience treating vaginismus, vulvodynia and other vulvovaginal disorders. She also has expertise in treating hypoactive sexual desire (low libido), arousal, and orgasmic disorders. Nell has lectured and written extensively on the topic of female sexual dysfunction and is a member of the Global Council for Research on Female Intimate Wellness.
• Nell practiced as a PA in psychiatry and orthopedic surgery before she became a female sexual medicine specialist. She is also a member of the Families of Overseas Servicemen Care Network and has volunteered in Vietnam providing medical care with Youth Hope Outreach Global (YHOG). Nell also studied at Carrow University in Australia and she spent two years living in Japan where she taught English with the Overseas Language Assistant Scheme.

```html
<!DOCTYPE html>
<html lang="en">
<head>
<meta charset="utf-8">
<title>Halden Pelvic Care Clinics – Brochure</title>
<link href="https://fonts.googleapis.com/css2?family=Open+Sans:wght@300;400;600;700&display=swap" rel="stylesheet">
<style>
:root{
  --stage:#a9aaad;
  --ink:#2f3550;
  --ink-soft:#4a4f66;
  --pink:#e2b0d2;
  --lavender:#e4daeb;
  --sky:#cee9f5;
  --white:#ffffff;
  --rule:#e7b9d2;
  --pill-pink:#e6b6d8;
  --pill-dark:#4c526a;
  --photo:#9d9d9d;
  --photo-light:#cbcbcb;
}
*{box-sizing:border-box;margin:0;padding:0}
html,body{width:796px;height:1200px;overflow:hidden;background:var(--stage)}
body{position:relative;font-family:"Open Sans",Arial,sans-serif;color:var(--ink)}
.spread{position:absolute;left:56px;width:684px;height:527px;background:var(--white);overflow:hidden}
.spread--outside{top:50px}
.spread--inside{top:623px}
.spread__bg{position:absolute;inset:0;width:100%;height:100%}
.panel{position:absolute;top:0;width:228px;height:527px}
.panel--1{left:0}.panel--2{left:228px}.panel--3{left:456px}
.panel-title{font-weight:300;font-size:19px;letter-spacing:.3px;color:var(--ink);text-transform:uppercase}
.centered{text-align:center}
.small{font-size:6.4px;line-height:1.35}
.body{font-size:6.8px;line-height:1.36}

/* Locations */
.locations{padding:22px 14px 0 58px}
.locations .panel-title{margin-left:-30px;text-align:center}
.loc-brand{font-size:10.5px;margin-top:16px;line-height:1.4}
.loc-rule{height:1px;background:var(--rule);margin:12px 6px}
.loc h3{font-weight:400;font-size:9px;margin-bottom:1px}
.loc p{font-size:7.6px;line-height:1.35}
.loc .small{margin-top:6px;font-size:6.4px}
.loc-note{font-size:7.4px;line-height:1.4;margin-left:-34px}

/* Books */
.books{padding:22px 14px 0 12px}
.books .panel-title{text-align:center;margin-bottom:12px}
.book{display:flex;gap:10px;padding:4px 0;border-bottom:1px solid var(--rule)}
.book:last-of-type{border-bottom:none}
.book__cover{flex:0 0 40px;height:54px}
.book p{font-size:5.9px;line-height:1.36}
.contact{text-align:center;margin-top:30px}
.contact .addr{font-size:6.6px;line-height:1.4}
.phone{display:flex;align-items:center;justify-content:center;gap:4px;font-size:11px;font-weight:400;margin-top:3px}
.phone svg{width:13px;height:13px}
.pill{display:inline-block;font-weight:700;font-size:8.6px;padding:3px 14px;border-radius:8px;background:var(--pill-pink);color:var(--ink)}
.contact .pill{margin-top:12px}

/* Cover */
.cover{padding:22px 10px 0 10px}
.cover .panel-title{text-align:right;line-height:.98;font-size:19px}
.cover-faces{position:absolute;left:10px;top:100px;display:flex;flex-direction:column;gap:5px}
.face{width:58px;height:58px;border-radius:50%}
.cover-info{position:absolute;left:88px;top:120px;width:138px;text-align:center}
.cover-cities{font-size:9.6px;font-weight:600;line-height:1.5}
.cover-rule{height:1px;background:var(--rule);margin:12px 10px}
.cover-text{font-size:7.4px;line-height:1.45}
.cover-contact{margin-top:36px}
.cover-contact .phone{font-size:12px;font-weight:600}
.cover-url{position:absolute;right:56px;bottom:8px;font-weight:700;font-size:10px;color:var(--ink-soft)}

/* Inside */
.inside{padding:26px 12px 0 18px}
.inside .panel-title{margin-bottom:16px}
.treat-list{list-style:none;margin-top:14px;padding-left:8px}
.treat-list li{font-size:6.9px;line-height:1.7;padding-left:10px;position:relative}
.treat-list li::before{content:"•";position:absolute;left:0}
.treat .pill{margin:24px 0 0 44px}
.philosophy ul{list-style:none}
.philosophy li{font-size:6.8px;line-height:1.38;padding-left:10px;position:relative;margin-bottom:10px}
.philosophy li::before{content:"•";position:absolute;left:0}
.bio{margin-bottom:14px;overflow:hidden}
.bio p{font-size:6.1px;line-height:1.4}
.bio b{font-weight:700}
.bio__photo{float:right;width:56px;height:56px;border-radius:50%;margin:0 0 4px 6px;shape-outside:circle(50%)}
.who .pill{position:absolute;left:60px;bottom:17px;background:var(--pill-dark);color:var(--white);font-size:9px;padding:3px 18px}
</style>
</head>
<body>

<section class="spread spread--outside">
  <svg class="spread__bg" viewBox="0 0 684 527" preserveAspectRatio="none" aria-hidden="true">
    <defs>
      <linearGradient id="wash" x1="0" y1="0" x2="0" y2="1">
        <stop offset="0" stop-color="#ffffff"/>
        <stop offset=".55" stop-color="#f6f1f8"/>
        <stop offset="1" stop-color="#e6dff0"/>
      </linearGradient>
      <linearGradient id="pinkband" x1="0" y1="0" x2="1" y2="0">
        <stop offset="0" stop-color="#e2b0d2"/>
        <stop offset="1" stop-color="#f1dcea"/>
      </linearGradient>
      <radialGradient id="lotusTone" cx=".5" cy=".6" r=".6">
        <stop offset="0" stop-color="#b9bdd6"/>
        <stop offset=".6" stop-color="#d3d4e6"/>
        <stop offset="1" stop-color="#e9e6f1" stop-opacity="0"/>
      </radialGradient>
    </defs>
    <rect width="684" height="527" fill="url(#wash)"/>
    <path d="M0 0 H60 C40 120 50 260 140 340 C80 300 20 220 0 150 Z" fill="url(#pinkband)" opacity=".85"/>
    <path d="M55 0 C40 110 60 240 150 320" fill="none" stroke="#cee9f5" stroke-width="8" opacity=".7"/>
    <path d="M228 0 H262 C250 60 240 130 200 200 C220 120 228 60 228 0 Z" fill="#e8c6de" opacity=".6"/>
    <path d="M430 0 H470 C470 120 440 220 456 290 C420 200 440 80 430 0 Z" fill="#e2b0d2" opacity=".75"/>
    <path d="M456 0 H510 C470 60 470 150 480 230 C455 140 456 60 456 0 Z" fill="#cee9f5" opacity=".8"/>
    <path d="M0 470 C150 440 260 500 380 480 C500 460 600 500 684 470 V527 H0 Z" fill="#e4daeb"/>
    <path d="M0 495 C180 470 300 520 684 490 V527 H0 Z" fill="#cee9f5" opacity=".8"/>
    <path d="M560 527 C600 490 650 470 684 465 V527 Z" fill="#e2b0d2"/>
    <rect x="227.5" y="0" width="1" height="527" fill="#ffffff" opacity=".6"/>
    <rect x="455.5" y="0" width="1" height="527" fill="#ffffff" opacity=".6"/>
  </svg>
  <svg class="spread__bg" viewBox="0 0 684 527" preserveAspectRatio="none" role="img" aria-label="Soft blue-grey lotus flowers floating on water across the lower panels">
    <ellipse cx="115" cy="455" rx="110" ry="55" fill="url(#lotusTone)"/>
    <ellipse cx="560" cy="465" rx="125" ry="60" fill="url(#lotusTone)"/>
  </svg>

  <div class="panel panel--1 locations">
    <h2 class="panel-title">Locations</h2>
    <p class="loc-brand centered">Halden Pelvic Care<br>Clinics</p>
    <div class="loc-rule"></div>
    <div class="loc centered">
      <h3>Main Office</h3>
      <p>14 Linden Circle NW, Suite 310<br>Washington, DC 20037<br>Phone: (202) 555-0143<br>Fax: (202) 555-0178</p>
      <p class="small">Across the street from<br>Linden Park University Hospital<br>and the Linden Park Metro</p>
    </div>
    <div class="loc-rule"></div>
    <div class="loc centered">
      <h3>New York Office:</h3>
      <p>62 East 39th Street, 7th floor<br>New York, NY 10016</p>
      <p class="small">Located one half block west<br>of Midtown Central Station</p>
    </div>
    <div class="loc-rule"></div>
    <div class="loc centered">
      <h3>New York Uptown Office:</h3>
      <p>7 E. 81st St. Suite 512<br>NY, NY 10028</p>
      <p class="small">Located on the Upper East Side,<br>steps from Museum Mile and<br>the 86th Street subway</p>
    </div>
    <div class="loc-rule"></div>
    <p class="loc-note centered">Our office in Washington DC is our main office and<br>all appointments and communications with all<br>three offices are made through this office.</p>
  </div>

  <div class="panel panel--2 books">
    <h2 class="panel-title">Our Books</h2>
    <div class="book">
      <div class="book__cover" role="img" aria-label="Book cover: When Intimacy Aches" style="background:linear-gradient(#f3efcf,#e2dca9)"></div>
      <p>When Intimacy Aches is a guide for patients that contains up-to-date information of more than the diagnosis and treatment on more than 20 different causes of sexual and vulvovaginal pain. It contains an algorithm that helps a patient and her health care provider determine the specific cause and treatment of her type of vulvar pain.</p>
    </div>
    <div class="book">
      <div class="book__cover" role="img" aria-label="Book cover: Pelvic Pain in Women" style="background:linear-gradient(#2e4a66,#15263a)"></div>
      <p>Pelvic Pain in Women: Diagnosis and Care is the only textbook devoted to the diagnosis and treatment of vulvar and vaginal pain disorders and disease. More than 75 worldrenowned scientists contributed chapters in this authoritative and comprehensive textbook.</p>
    </div>
    <div class="book">
      <div class="book__cover" role="img" aria-label="Book cover: Rekindled" style="background:linear-gradient(#e4eef0,#c6d8db)"></div>
      <p>Rekindled: 4 Steps Back to Desire outlines a highly effective holistic approach to treating decreased sexual desire. In addition, there is essential information on the ways in which major life events such as pregnancy, menopause, and divorce can affect a woman's sexual health.</p>
    </div>
    <div class="book">
      <div class="book__cover" role="img" aria-label="Book cover: Together" style="background:linear-gradient(#cf5a55,#b8423f)"></div>
      <p>Together: A Closer Look at Commitment: the author explains our non-monogamous instincts from an evolutionary perspective. Men and women are guided with compassion and wisdom in understanding their natural sexual tendencies to allow them to cultivate more sexy lovemaking -even in long-term, monogamous relationships!</p>
    </div>
    <div class="book">
      <div class="book__cover" role="img" aria-label="Book cover: Answers About Vulvar and Vaginal Cancer" style="background:linear-gradient(#f4d3df,#e6a9c0)"></div>
      <p>Answers About Vulvar and Vaginal Cancer and Other Diseases of the Vulva and Vagina: provides practical, authoritative answers to the most common questions asked by women diagnosed with cancer of the vulva/vagina and related gynecologic diseases.</p>
    </div>
    <div class="contact">
      <p class="addr">7 E. 81st St. Suite 512 NY<br>NY 10028</p>
      <p class="phone"><svg viewBox="0 0 24 24" aria-hidden="true"><path d="M7 2c-2 1-4 3-3 7 2 6 6 11 12 13 3 1 5-1 6-3l-4-4-3 2c-3-1-6-5-7-8l2-3z" fill="#2f3550"/></svg>(202) 555-0143</p>
      <span class="pill">www.haldenpelvic.org</span>
    </div>
  </div>

  <div class="panel panel--3 cover">
    <h1 class="panel-title">Halden Pelvic<br>Care Clinics</h1>
    <div class="cover-faces">
      <div class="face" role="img" aria-label="Portrait photo of a smiling woman" style="background:radial-gradient(circle at 50% 40%,var(--photo-light),#5b5b5b)"></div>
      <div class="face" role="img" aria-label="Portrait photo of a woman resting her chin on her hand" style="background:radial-gradient(circle at 50% 40%,#e2e2e2,var(--photo))"></div>
      <div class="face" role="img" aria-label="Portrait photo of a laughing woman" style="background:radial-gradient(circle at 50% 40%,var(--photo-light),#4a4a4a)"></div>
      <div class="face" role="img" aria-label="Portrait photo of a woman with short hair" style="background:radial-gradient(circle at 50% 40%,#d6d6d6,#6f6f6f)"></div>
      <div class="face" role="img" aria-label="Portrait photo of a smiling woman with dark hair" style="background:radial-gradient(circle at 50% 40%,#bdbdbd,#3d3d3d)"></div>
      <div class="face" role="img" aria-label="Portrait photo of a young woman" style="background:radial-gradient(circle at 50% 40%,#e6e6e6,var(--photo))"></div>
    </div>
    <div class="cover-info">
      <p class="cover-cities">Washington DC<br>New York<br>Upper East Side NY</p>
      <div class="cover-rule"></div>
      <p class="cover-text">For more than two decades, Halden Pelvic Care Clinics have been referral centers for the treatment of vulvodynia, sexual pain disorders, dermatologic diseases of the vulva, recurrent vulvovaginal infections, and female sexual dysfunction.</p>
      <div class="cover-contact">
        <p class="small">7 E. 81st St. Suite 512 NY<br>NY 10028</p>
        <p class="phone"><svg viewBox="0 0 24 24" aria-hidden="true"><path d="M7 2c-2 1-4 3-3 7 2 6 6 11 12 13 3 1 5-1 6-3l-4-4-3 2c-3-1-6-5-7-8l2-3z" fill="#2f3550"/></svg>(202) 555-0143</p>
      </div>
    </div>
    <p class="cover-url">www.haldenpelvic.org</p>
  </div>
</section>

<section class="spread spread--inside">
  <svg class="spread__bg" viewBox="0 0 684 527" preserveAspectRatio="none" aria-hidden="true">
    <defs>
      <linearGradient id="wash2" x1="0" y1="0" x2="0" y2="1">
        <stop offset="0" stop-color="#ffffff"/>
        <stop offset=".5" stop-color="#f3eef7"/>
        <stop offset="1" stop-color="#e4daeb"/>
      </linearGradient>
      <radialGradient id="lotusTone2" cx=".5" cy=".6" r=".6">
        <stop offset="0" stop-color="#b4b8d3"/>
        <stop offset=".6" stop-color="#d0d2e5"/>
        <stop offset="1" stop-color="#e9e6f1" stop-opacity="0"/>
      </radialGradient>
    </defs>
    <rect width="684" height="527" fill="url(#wash2)"/>
    <path d="M0 0 H684 V22 C560 40 420 8 300 24 C180 40 80 18 0 30 Z" fill="#e2b0d2"/>
    <path d="M0 30 C80 18 180 40 300 24 C420 8 560 40 684 22 V34 C560 50 420 18 300 34 C180 50 80 28 0 40 Z" fill="#cee9f5"/>
    <path d="M0 480 C160 450 300 505 450 480 C560 462 630 490 684 475 V527 H0 Z" fill="#e4daeb"/>
    <path d="M0 500 C200 475 360 520 684 495 V527 H0 Z" fill="#e2b0d2" opacity=".85"/>
    <path d="M0 515 C220 500 420 527 684 510 V527 H0 Z" fill="#cee9f5"/>
    <rect x="227.5" y="0" width="1" height="527" fill="#ffffff" opacity=".6"/>
    <rect x="455.5" y="0" width="1" height="527" fill="#ffffff" opacity=".6"/>
  </svg>
  <svg class="spread__bg" viewBox="0 0 684 527" preserveAspectRatio="none" role="img" aria-label="Faint lotus flowers on water along the bottom of the inside panels">
    <ellipse cx="250" cy="470" rx="170" ry="55" fill="url(#lotusTone2)"/>
  </svg>

  <div class="panel panel--1 inside treat">
    <h2 class="panel-title">What We Treat</h2>
    <p class="body">The physicians of Halden Pelvic Care Clinics are experts in the diagnosis and treatment of more than two dozen diseases that cause the symptoms of genital itching, burning, irritation, rawness, throbbing, urinary frequency and urgency, and pain during sex. The diseases we treat include:</p>
    <ul class="treat-list">
      <li>Pain With Sex</li>
      <li>Vaginal and Vulvar Discomfort</li>
      <li>Burning, Rawness, Itching &amp; Pain</li>
      <li>Vulvodynia</li>
      <li>Vulvar Vestibulitis (Vestibulodynia)</li>
      <li>Vulvovaginal Skin Diseases</li>
      <li>Lichen Sclerosus</li>
      <li>Lichen Planus</li>
      <li>VIN</li>
      <li>Lichen Simplex Chronicus</li>
      <li>Plasma Cell Vulvitis</li>
      <li>Pudendal Neuralgia</li>
      <li>Chronic Pelvic Pain</li>
      <li>Persistant Genital Arousal Disorder</li>
      <li>Decreased Libido</li>
      <li>Decreased Orgasm</li>
      <li>Decreased Arousal</li>
      <li>Pelvic Floor Muscle Dysfunction</li>
      <li>Vaginismus</li>
      <li>Interstitial Cystitis/Painful Bladder Syndrome</li>
    </ul>
    <span class="pill">www.haldenpelvic.org</span>
  </div>

  <div class="panel panel--2 inside philosophy">
    <h2 class="panel-title">Our Philosophy</h2>
    <ul>
      <li>It is our belief that quality medical care cannot be rushed. By taking a comprehensive medical history, we give our patients the opportunity to be heard.</li>
      <li>We pride ourselves on our precise physical examinations, diagnostic precision and effective treatment. With the use of specialized testing and extensive research, we have developed algorithms to achieve accuracy and specificity in our diagnoses and therapies.</li>
      <li>Patient education is critical to our treatment process. We ensure that our patients have their questions answered and are connected with reliable resources. As a result, our patients are given a sense of hope and empowerment.</li>
      <li>We believe in the importance of experience and expertise. It is imperative for us to stay current with the latest literature, to focus our attention exclusively on vulvovaginal disorders and to invest a great deal of our own time and resources on research. We conduct over a dozen medical studies each year to find new treatments for vulvovaginal diseases.</li>
      <li>In our effort to provide the best care possible, we employ a multidisciplinary approach to treatment. To accomplish this, we enlist the help of our colleagues in other arenas of sexual health care including physical therapists, sex therapists, psychologists, and nutritionists.</li>
    </ul>
  </div>

  <div class="panel panel--3 inside who">
    <h2 class="panel-title">Who We Are</h2>
    <div class="bio">
      <div class="bio__photo" role="img" aria-label="Portrait photo of Dr. Owen Hartwell" style="background:radial-gradient(circle at 50% 40%,#d8c4b4,#5a4a42)"></div>
      <p><b>Dr. Owen Hartwell</b> has been the director of the HPCC since 2002. He is the current President of the Global Council for Research on Female Intimate Wellness. In addition, he is a Fellow of IAVD, ACCP, and STRA. Dr. Hartwell has been a grant recipient of the Vulvar Health Foundation. He is actively involved in research and has published more than 75 abstracts, peerreviewed articles, and book chapters. He is also co-author of When Intimacy Aches, Pelvic Pain in Women: Diagnosis and Care, and Rekindled: 4 Steps Back to Desire.</p>
    </div>
    <div class="bio">
      <div class="bio__photo" role="img" aria-label="Portrait photo of Dr. Celia Marsh" style="background:radial-gradient(circle at 50% 40%,#ecdcc6,#8d7a66)"></div>
      <p><b>Dr. Celia Marsh</b> completed her Ob/Gyn residency at Carlisle Medical and also completed a fellowship in Female Pelvic Medicine and Reconstructive Surgery at the University of Brentmoor. She is regarded as an expert in the evaluation and treatment of female pelvic floor disorders and interstitial cystitis.</p>
    </div>
    <div class="bio">
      <div class="bio__photo" role="img" aria-label="Portrait photo of Nell Brisco, PA-C" style="background:radial-gradient(circle at 50% 40%,#f0dcc6,#b08a6a)"></div>
      <p><b>Nell Brisco</b> is a Nationally Certified Physician Assistant licensed in New York and Washington, DC. She graduated with honors from Wexley College of Health Sciences where she was awarded the prestigious Pemberton Award. Nell has been treating women with sexual dysfunction since 2010. She has extensive experience treating vaginismus, vulvodynia and other vulvovaginal disorders. She also has expertise in treating hypoactive sexual desire (low libido), arousal, and orgasmic disorders. Nell has lectured and written extensively on the topic of female sexual dysfunction and is a member of the Global Council for Research on Female Intimate Wellness.</p>
    </div>
    <span class="pill">www.haldenpelvic.org</span>
  </div>
</section>

</body>
</html>
```